Kelro DIGITAL HORIZON learning portal

We beed a flyer design to launch our new DIGITAL HORIZON Learning Portal. The flyer will be used in letter box drops and to give to small business to encourage sales of this new service.

ABOUT US:

We are a small training firm offering world class training solutions in the areas of:

1. Time Management
2. Sales skills
3. Strategic & High performance leadership
4. Sales Management
5. Personal Maximum Achievement.

You can find our website at www.kelro-example.com.au

ABOUT DIGITAL HORIZON Learning Portal:

We are launching an online learning portal called DIGITAL HORIZON Learning Portal which will allow anyone, anywhere in the world to take our courses online as long as they have access to a PC, smart phone and internet.

Taking an online course with Kelro through our DIGITAL HORIZON Learning Portal will allow students/participants to save over 50% of the normal price of attending a face to face training program.

There are over 80 different individual learning units that can be taken by a student/participant. The participant can choose to take any unit they wish building their own unique learning experience or they can take a full course in one of the subject areas listed above in the about us section.

ADVANTAGES OF USING THE Kelro DIGITAL HORIZON Learning Portal:

* Cost effective, save over 50% by learning online compared to attending a Kelro class room based programme.
* learning can be scheduled around work and family
* Reduces travel time and travel costs
* Students/participants have the option to select learning materials that meets their level of knowledge and interest.
* Complete flexibility to build a personalised learning experience.
* Students/participants can study anywhere they have access to a computer and Internet connection
* Self-paced learning modules allow students/participants to work at their own pace
* Develops knowledge of the Internet and computers skills that will help learners throughout their lives and careers
* Successfully completing online or computer-based courses builds self-knowledge and self-confidence and encourages students to take responsibility for their learning
* Join over 4 million people who have successfully undertaken the training world wide at a time & a place convenient to students/participants.
* pay securely using swiftcoin
* learn based on a students/participants personal financial circumstances with individual units priced at $82.50 each (this is Australian dollars & includes GST)

The final design will be one that conveys flexibility of learning, cost effectiveness of the online learning solution. The flyer design can either be folded, single or double sided, A4 or A5 or DL size - whatever works best in the final outcome.

Industry/Entity Type

Small Business

Requirements
Must have
• The flyer must include:

* the "DIGITAL HORIZON Learning portal" logo and the "Kelro logo" and use the Kelro font. Several logos have been provided and the most appropriate ones can be chosen for the design. The font has been provided. (I do have other logo files in different file formats if required to aid designers)

* The flyer must direct people to the Kelro website www.kelro-example.com.au to pay, enrol and find out other information about the courses.

* The flyer must highlight cost effectiveness of the solution, the world wide popularity of the programs (over 4 million people have completed the programs world wide), flexibility of learning & the diversity of study areas.

Because of price changes in future of courses it would be very beneficial to be able to edit files in future to show new prices if and when that happens.

```html
<!DOCTYPE html>
<html lang="en">
<head>
<meta charset="utf-8">
<title>Kelro – DIGITAL HORIZON Learning Portal flyer</title>
<link rel="stylesheet" href="https://fonts.googleapis.com/css2?family=Pathway+Gothic+One&family=Signika:wght@400;600&family=Indie+Flower&family=Tinos&display=swap">
<style>
  :root {
    --ink: #111111;
    --sky: #3a8ff0;
    --teal: #23b3a6;
    --mark: #2bb7b0;
    --grey-name: #555a5a;
    --navy: #1f3f7a;
    --paper: #f4f6f8;
    --sea-light: #cfe8fb;
    --sea-deep: #1d7fd6;
  }
  html, body { margin: 0; padding: 0; overflow: hidden; }
  body { width: 848px; height: 1200px; }
  .flyer {
    position: relative;
    width: 848px;
    height: 1200px;
    overflow: hidden;
    background:
      linear-gradient(160deg, rgba(255,255,255,0.9) 0%, rgba(230,234,238,0.6) 30%, rgba(255,255,255,0.85) 45%, rgba(232,236,240,0.5) 65%, #ffffff 80%),
      var(--paper);
  }
  .brand {
    position: absolute; left: 62px; top: 52px;
    display: flex; flex-direction: column; align-items: center; gap: 8px;
  }
  .brand-square { width: 80px; height: 80px; background: var(--mark); border-radius: 6px; }
  .brand-name {
    font-family: "Signika", sans-serif; font-weight: 400;
    font-size: 32px; color: var(--grey-name); line-height: 1;
  }
  .headline {
    position: absolute; right: 52px; top: 50px; margin: 0;
    text-align: right;
    font-family: "Pathway Gothic One", sans-serif; font-weight: 400;
    font-size: 46px; line-height: 50px; color: var(--ink);
  }
  .headline .accent { color: var(--sky); }
  .tagline {
    position: absolute; left: 72px; top: 302px; margin: 0;
    font-family: "Pathway Gothic One", sans-serif;
    font-size: 42px; color: var(--teal); font-weight: 400;
  }
  .screen-visual {
    position: absolute; left: 561px; top: 336px; width: 287px; height: 370px;
    background: linear-gradient(180deg, #2a2a2a 0%, #2a2a2a 60%, #d9dcdf 61%, #eef0f2 100%);
  }
  .save-note {
    position: absolute; left: 738px; top: 400px; margin: 0;
    font-family: "Indie Flower", cursive; font-size: 36px; line-height: 52px;
    color: var(--ink); text-align: center; width: 100px;
    background: #f7f7f7;
  }
  .save-note .accent { color: var(--sky); }
  .offer {
    position: absolute; left: 48px; top: 578px; margin: 0;
    font-family: "Signika", sans-serif; font-weight: 600;
    font-size: 25px; color: var(--ink);
  }
  .courses {
    position: absolute; left: 48px; top: 640px; margin: 0; padding: 0;
    list-style: none;
    font-family: "Signika", sans-serif; font-weight: 600;
    font-size: 27px; line-height: 31px; color: var(--sky);
  }
  .payment {
    position: absolute; left: 600px; top: 800px; width: 200px; text-align: center;
  }
  .payment-label { font-family: "Tinos", serif; font-size: 15px; color: var(--ink); margin: 0; }
  .payment-name {
    font-family: "Signika", sans-serif; font-weight: 600;
    font-size: 30px; color: var(--navy); margin: 2px 0 0;
  }
  .sea-visual {
    position: absolute; left: 0; top: 880px; width: 848px; height: 320px;
    background:
      radial-gradient(ellipse at 35% 45%, rgba(255,255,255,0.9) 0%, rgba(255,255,255,0) 45%),
      linear-gradient(180deg, rgba(255,255,255,0) 0%, var(--sea-light) 25%, #7cc0f2 55%, var(--sea-deep) 80%, #e9f3fb 100%);
  }
  .register {
    position: absolute; left: 37px; top: 1152px; margin: 0;
    font-family: "Tinos", serif; font-size: 20px; color: var(--ink);
  }
  .register .url { font-size: 23px; }
  .portal-badge {
    position: absolute; left: 585px; top: 1122px; width: 246px; height: 54px;
    display: flex; align-items: center; gap: 10px;
  }
  .portal-square { width: 44px; height: 44px; background: var(--navy); }
  .portal-name {
    font-family: "Signika", sans-serif; font-weight: 600;
    font-size: 22px; color: var(--navy); white-space: nowrap;
  }
</style>
</head>
<body>
  <main class="flyer">
    <div class="brand">
      <div class="brand-square"></div>
      <span class="brand-name">Kelro</span>
    </div>

    <h1 class="headline">
      Join over <span class="accent">4 million</span> people<br>
      who have successfully undertaken<br>
      the online training <span class="accent">world wide</span>
    </h1>

    <p class="tagline">Study anywhere, anytime</p>

    <div class="screen-visual" role="img" aria-label="Computer monitor showing an open book resting on a stack of books"></div>
    <p class="save-note">Save<br>upto<br><span class="accent">50%</span></p>

    <p class="offer">We are offering world class training in</p>
    <ul class="courses">
      <li>Time Management</li>
      <li>Sales skills</li>
      <li>Strategic &amp; High performance leadership</li>
      <li>Sales Management</li>
      <li>Personal Maximum Achievement</li>
    </ul>

    <div class="payment">
      <p class="payment-label">Secure Payments by</p>
      <p class="payment-name">SwiftCoin</p>
    </div>

    <div class="sea-visual" role="img" aria-label="Soft blue abstract water splash with light streaks"></div>

    <p class="register">register at <span class="url">www.kelro-example.com.au</span></p>

    <div class="portal-badge">
      <div class="portal-square"></div>
      <span class="portal-name">DIGITAL HORIZON</span>
    </div>
  </main>
</body>
</html>
```